Instagram background for quotes

We need a 1080x1080 background for instagram. I use the Phonto app to put text over the image.

We create motivating and inspiring messages for our followers on IG.

Our brands message is, "Mediocre thinking leads to mediocre results. Get Mission - Get Motivated - Get Moving
https://www.example-social.test/steel_resolve_co/

We would like to move away from the rustic look and have a gloss black background with the goal of using text that is cleaner to match the SR in the logo.

I see the design remaining fairly close to what it is now with the logo at the top. I like the quotes on this brand here, https://www.example-social.test/talkwithtycoons/?hl=en. I see this being built into our new background with the quotations being aggressive to match the wings in our logo.

Here is another brand we like - https://www.example-social.test/boomboomdrive/

I've attached the files I was given by the logo designer who has disappeared. I am hoping what is there will suffice.

Target Market(s)

24-34 year old males

Industry/Entity Type

Quotes

Colors
000000
ffffff

Requirements
Must have
• Provided Logo without text
Nice to have
• Aggressive looking quotes to match wings
• Watermark logo in background

```html
<!DOCTYPE html>
<html lang="en">
<head>
<meta charset="utf-8">
<title>Prioritize and Execute — Quote Post</title>
<link rel="stylesheet" href="https://fonts.googleapis.com/css2?family=Bebas+Neue&display=swap">
<style>
  :root {
    --stage: #808080;
    --post-black: #000000;
    --ink-white: #ffffff;
    --watermark: #141414;
  }
  * { margin: 0; padding: 0; box-sizing: border-box; }
  html, body {
    width: 1200px;
    height: 1000px;
    overflow: hidden;
    background: var(--stage);
  }
  .canvas {
    position: relative;
    width: 1200px;
    height: 1000px;
    background: var(--stage);
    font-family: "Bebas Neue", "Oswald", sans-serif;
  }
  .quote-post {
    position: absolute;
    left: 387px;
    top: 287px;
    width: 425px;
    height: 425px;
    background: var(--post-black);
    overflow: hidden;
  }
  .post-frame {
    position: absolute;
    inset: 0;
    width: 425px;
    height: 425px;
  }
  .post-frame line {
    stroke: var(--ink-white);
    stroke-width: 2;
  }
  .brand-watermark {
    position: absolute;
    left: 0;
    right: 0;
    top: 60px;
    text-align: center;
    font-size: 330px;
    line-height: 1;
    color: var(--watermark);
    letter-spacing: 6px;
  }
  .brand-mark {
    position: absolute;
    left: 0;
    right: 0;
    top: 6px;
    text-align: center;
    font-size: 50px;
    line-height: 1;
    color: var(--ink-white);
    letter-spacing: 3px;
  }
  .quote {
    position: absolute;
    left: 0;
    right: 0;
    top: 128px;
    text-align: center;
    color: var(--ink-white);
    line-height: 1;
  }
  .quote .line-major {
    display: block;
    font-size: 62px;
    letter-spacing: 0.5px;
  }
  .quote .line-minor {
    display: block;
    font-size: 34px;
    margin: 6px 0 8px;
  }
  .hashtag {
    position: absolute;
    right: 32px;
    top: 394px;
    font-size: 21px;
    line-height: 1;
    color: var(--ink-white);
    letter-spacing: 0.3px;
  }
</style>
</head>
<body>
<div class="canvas">
  <section class="quote-post">
    <div class="brand-watermark" aria-hidden="true">SR</div>

    <svg class="post-frame" viewBox="0 0 425 425" aria-hidden="true">
      <line x1="20" y1="21" x2="140" y2="21"/>
      <line x1="283" y1="21" x2="405" y2="21"/>
      <line x1="20" y1="20" x2="20" y2="405"/>
      <line x1="405" y1="20" x2="405" y2="405"/>
      <line x1="19" y1="404" x2="238" y2="404"/>
      <line x1="398" y1="404" x2="406" y2="404"/>
    </svg>

    <div class="brand-mark">SR</div>

    <h1 class="quote">
      <span class="line-major">Prioritize</span>
      <span class="line-minor">And</span>
      <span class="line-major">Execute</span>
    </h1>

    <p class="hashtag">#SteelResolve</p>
  </section>
</div>
</body>
</html>
```